Eiskarte für Landhotel
Zielgruppe
Landhotel und Restaurant, Sommergarten, Biergarten
Aufgabenstellung
Eiskarte:
Ländlich, Bäuerlich, Vintage, gepflegte Küche

```html
<!DOCTYPE html>
<html lang="de">
<head>
<meta charset="utf-8">
<title>Eiskarte – Landhotel Waldrose</title>
<link rel="stylesheet" href="https://fonts.googleapis.com/css2?family=Josefin+Sans:wght@300&family=Yellowtail&display=swap">
<style>
  :root {
    --cream: #fdf7d0;
    --salmon: #f19a7c;
    --salmon-dark: #d9735c;
    --green: #a8d68b;
    --green-line: #9dcf7f;
    --badge-white: #fffdf3;
    --grey: #7a7a7a;
    --cup-pink: #f6c3b3;
    --cup-green: #c4e0a9;
  }
  * { margin: 0; padding: 0; box-sizing: border-box; }
  html, body { width: 848px; height: 1200px; overflow: hidden; background: var(--cream); }
  .menu-cover { position: relative; width: 848px; height: 1200px; background: var(--cream); }
  .frame, .awning, .title { position: absolute; left: 0; top: 0; }
  .brand-name {
    position: absolute; left: 265px; top: 111px; width: 320px; height: 320px;
    display: flex; flex-direction: column; align-items: center; justify-content: center;
    font-family: "Josefin Sans", sans-serif; font-weight: 300; color: var(--grey);
    letter-spacing: 6px; font-size: 30px; line-height: 1.4; text-align: center;
  }
  .corner-ornament {
    position: absolute; width: 86px; height: 92px; border-radius: 40px;
    background: radial-gradient(circle, var(--cream) 25%, var(--green) 70%);
    opacity: .85;
  }
  .corner-ornament.top-left { left: 28px; top: 64px; }
  .corner-ornament.top-right { right: 28px; top: 64px; }
  .corner-ornament.bottom-left { left: 28px; top: 1064px; }
  .corner-ornament.bottom-right { right: 28px; top: 1064px; }
  .sundae-illustration {
    position: absolute; left: 306px; top: 720px; width: 307px; height: 342px;
    border-radius: 48% 48% 30% 30%;
    background: linear-gradient(180deg, var(--salmon) 0%, var(--cup-green) 30%, var(--cup-pink) 60%, var(--cream) 100%);
    opacity: .8;
  }
</style>
</head>
<body>
<main class="menu-cover">
  <svg class="frame" width="848" height="1200" viewBox="0 0 848 1200" aria-hidden="true">
    <g stroke="var(--green-line)" fill="none">
      <line x1="185" y1="67" x2="663" y2="67" stroke-width="2.5"/>
      <line x1="185" y1="74" x2="663" y2="74" stroke-width="1.2"/>
      <line x1="185" y1="1133" x2="663" y2="1133" stroke-width="1.2"/>
      <line x1="185" y1="1140" x2="663" y2="1140" stroke-width="2.5"/>
      <line x1="29" y1="185" x2="29" y2="1025" stroke-width="2.5"/>
      <line x1="819" y1="185" x2="819" y2="1025" stroke-width="2.5"/>
    </g>
    <g fill="var(--green-line)">
      <path d="M29 575 l6 25 -6 25 -6 -25 Z"/>
      <path d="M819 575 l6 25 -6 25 -6 -25 Z"/>
    </g>
  </svg>

  <div class="corner-ornament top-left" role="img" aria-label="Rankenornament mit Blättern"></div>
  <div class="corner-ornament top-right" role="img" aria-label="Rankenornament mit Blättern"></div>
  <div class="corner-ornament bottom-left" role="img" aria-label="Rankenornament mit Blättern"></div>
  <div class="corner-ornament bottom-right" role="img" aria-label="Rankenornament mit Blättern"></div>

  <svg class="awning" width="848" height="1200" viewBox="0 0 848 1200" aria-hidden="true">
    <g>
      <path fill="var(--salmon)" d="M54 88 H136 V395 a41 41 0 0 1 -82 0 Z"/>
      <path fill="var(--green)"  d="M136 88 H219 V395 a41 41 0 0 1 -83 0 Z"/>
      <path fill="var(--salmon)" d="M219 88 H301 V395 a41 41 0 0 1 -82 0 Z"/>
      <path fill="var(--green)"  d="M301 88 H383 V395 a41 41 0 0 1 -82 0 Z"/>
      <path fill="var(--salmon)" d="M383 88 H466 V395 a41 41 0 0 1 -83 0 Z"/>
      <path fill="var(--green)"  d="M466 88 H548 V395 a41 41 0 0 1 -82 0 Z"/>
      <path fill="var(--salmon)" d="M548 88 H630 V395 a41 41 0 0 1 -82 0 Z"/>
      <path fill="var(--green)"  d="M630 88 H713 V395 a41 41 0 0 1 -83 0 Z"/>
      <path fill="var(--salmon)" d="M713 88 H795 V395 a41 41 0 0 1 -82 0 Z"/>
    </g>
    <circle cx="425" cy="271" r="160" fill="var(--badge-white)"/>
  </svg>

  <div class="brand-name"><span>LANDHOTEL</span><span>WALDROSE</span></div>

  <svg class="title" width="848" height="1200" viewBox="0 0 848 1200">
    <g font-family="Yellowtail, cursive" font-size="170" text-anchor="middle" stroke-linejoin="round">
      <text x="430" y="655" fill="var(--green)" stroke="var(--green)" stroke-width="38">Eiskarte</text>
      <text x="424" y="648" fill="var(--badge-white)" stroke="var(--badge-white)" stroke-width="26">Eiskarte</text>
      <text x="424" y="648" fill="var(--salmon)" stroke="var(--salmon-dark)" stroke-width="3" paint-order="stroke">Eiskarte</text>
    </g>
  </svg>

  <div class="sundae-illustration" role="img" aria-label="Illustration eines Eisbechers mit drei Kugeln und einem Löffel"></div>
</main>
</body>
</html>
```